Marigold Premium Business Card Design Project

About the company: Here at Fernhaven Botanics, we focus on cosmetic products that based on essential oils and different kinds of plant essences. All of our raw materials are pure organic and specially selected from local producers in Australia.

I'm here to look for a unique business card design, to replace the current one later on, so I don't have many requirements. Why I wanna restrict designers' creativity?

All I know is: 1. do not make it too complicated, straight forward, simple and pure. 2. this design may be used for other purposes (i.e. logo and slogan on the front, Brand Story and contact details at the back). Therefor, I'd like to have the design for 3 layouts, one only have logo, slogan, contact detials, one for the brand story, the other one for the personal business card with staff's mob etc...

A vector graphic is required, i.e. eps, ai, easy for me to resize.

Round Corner.

Thanks

Plz add "Hand made in Australia" in the design, cheers.

Target Market(s)

Women aged yr 20-50

Industry/Entity Type

Business

Requirements
Must have
• Logo: please see attacment (eps, ai)

Slogan: Moonlit Velvet Glow

Website:www.fernhavenbotanics.com.au

Address: temporary not available

Phone: temporary not available

"Hand made in Australia"

Nice to have
• Prefer round corner

```html
<!DOCTYPE html>
<html lang="en">
<head>
<meta charset="utf-8">
<title>Fernhaven Botanics – Business Card Options</title>
<link rel="stylesheet" href="https://fonts.googleapis.com/css2?family=Marcellus&family=Open+Sans:wght@400&display=swap">
<style>
  :root {
    --stage: #5b3b24;
    --label: #ffffff;
    --card-white: #ffffff;
    --card-black: #1d1a1b;
    --card-pink: #f9dce6;
    --brand-pink: #d4497a;
    --ink: #2b2b2b;
    --ink-soft: #3a3a3a;
    --ink-light: #dddddd;
    --ink-on-pink: #4a4a4a;
  }
  html, body {
    margin: 0;
    padding: 0;
    overflow: hidden;
  }
  body {
    width: 1200px;
    height: 784px;
    background: var(--stage);
    position: relative;
    font-family: "Marcellus", serif;
  }
  .option-label {
    position: absolute;
    margin: 0;
    color: var(--label);
    font-family: "Open Sans", sans-serif;
    font-size: 22px;
    font-weight: 400;
  }
  .label-1 { left: 52px; top: 6px; }
  .label-2 { left: 40px; top: 712px; }
  .label-3 { left: 608px; top: 708px; }

  .card {
    position: absolute;
    width: 536px;
    height: 304px;
    border-radius: 24px;
    box-shadow: 0 4px 10px rgba(0, 0, 0, 0.35);
    text-align: center;
  }
  .card-front-white { left: 40px; top: 58px; background: var(--card-white); }
  .card-personal   { left: 604px; top: 52px; height: 306px; background: var(--card-white); }
  .card-front-black { left: 38px; top: 396px; width: 534px; height: 302px; background: var(--card-black); }
  .card-front-pink { left: 598px; top: 390px; background: var(--card-pink); }

  .brand-name {
    position: absolute;
    left: 0;
    right: 0;
    margin: 0;
    color: var(--brand-pink);
    font-family: "Marcellus", serif;
    font-size: 46px;
    font-weight: 400;
    line-height: 1;
  }
  .card-front-white .brand-name,
  .card-front-black .brand-name,
  .card-front-pink .brand-name { top: 120px; }
  .card-personal .brand-name { top: 68px; font-size: 40px; }

  .slogan {
    position: absolute;
    left: 0;
    right: 0;
    margin: 0;
    font-size: 23px;
    letter-spacing: 1px;
    text-transform: uppercase;
  }
  .card-front-white .slogan { top: 246px; color: var(--ink); font-size: 21px; }
  .card-front-black .slogan { top: 252px; color: var(--ink-light); }
  .card-front-pink .slogan { top: 252px; color: var(--ink-on-pink); }

  .staff-name {
    position: absolute;
    left: 0; right: 0; top: 198px;
    margin: 0;
    color: var(--ink);
    font-size: 22px;
    font-weight: 400;
    text-transform: uppercase;
  }
  .staff-role {
    position: absolute;
    left: 0; right: 0; top: 228px;
    margin: 0;
    color: var(--ink-soft);
    font-family: "Open Sans", sans-serif;
    font-size: 12px;
  }
  .contact {
    position: absolute;
    left: 0; right: 0; top: 260px;
    margin: 0;
    color: var(--ink-soft);
    font-family: "Open Sans", sans-serif;
    font-size: 12.5px;
    line-height: 19px;
    font-style: normal;
  }
</style>
</head>
<body>

  <p class="option-label label-1">front Option 1</p>

  <section class="card card-front-white">
    <h2 class="brand-name">Fernhaven Botanics</h2>
    <p class="slogan">Moonlit Velvet Glow</p>
  </section>

  <section class="card card-personal">
    <h2 class="brand-name">Fernhaven Botanics</h2>
    <h3 class="staff-name">Your Name Here</h3>
    <p class="staff-role">Designation</p>
    <address class="contact">
      Fern Lane, Suite 500, City name, Country name 678.<br>
      Phone: 200 555 0147. &nbsp;&nbsp;www.FERNHAVENBOTANICS.com.au
    </address>
  </section>

  <section class="card card-front-black">
    <h2 class="brand-name">Fernhaven Botanics</h2>
    <p class="slogan">Moonlit Velvet Glow</p>
  </section>

  <section class="card card-front-pink">
    <h2 class="brand-name">Fernhaven Botanics</h2>
    <p class="slogan">Moonlit Velvet Glow</p>
  </section>

  <p class="option-label label-2">front &nbsp;Option 2</p>
  <p class="option-label label-3">front &nbsp;Option 3</p>

</body>
</html>
```